Criação de Peça Gráfica (unidade) para Segurança & Vigilância
A empresa queria:
" Fornecemos, alugamos, instalamos e damos manutenção, bem como, fornecemos mão de obra alocada residente para que o nosso cliente tenha total conforto e segurança. "

```html
<!DOCTYPE html>
<html lang="pt-BR">
<head>
<meta charset="UTF-8">
<title>Sistemas Especiais Integrados – Folder</title>
<link href="https://fonts.googleapis.com/css2?family=Roboto:wght@400;500;700;900&family=Roboto+Condensed:wght@400;700&display=swap" rel="stylesheet">
<style>
  :root{
    --stage:#e9ecef;
    --paper:#f2f7fc;
    --blue:#1a8fe3;
    --blue-deep:#0d4f9c;
    --navy:#0b2f63;
    --panel:rgba(14,44,96,0.82);
    --panel-line:rgba(120,190,255,0.5);
    --ink:#0b2a55;
    --white:#ffffff;
  }
  *{box-sizing:border-box;margin:0;padding:0}
  html,body{width:1200px;height:1200px;overflow:hidden;background:var(--stage)}
  body{font-family:"Roboto",Arial,sans-serif;position:relative}
  .brochure{position:absolute;left:20px;top:198px;width:1160px;height:805px;background:var(--paper);overflow:hidden;box-shadow:0 6px 24px rgba(0,0,0,.15)}
  .brochure__bg{position:absolute;inset:0}
  .placeholder{position:absolute}
  .network-art{left:0;top:0;width:330px;height:640px;background:radial-gradient(circle at 40% 40%,#5fb4f0 0%,#2b7fd0 40%,rgba(220,236,250,0.2) 85%);opacity:.85}
  .network-art--corner{left:880px;top:600px;width:280px;height:205px;background:radial-gradient(circle at 70% 70%,#3a95e6 0%,rgba(220,236,250,0) 75%)}
  .portrait{left:600px;top:570px;width:200px;height:235px;background:linear-gradient(180deg,#dbe4ee 0%,#3a4656 60%,#1d2430 100%)}
  .section-title{position:absolute;left:305px;top:50px;font-family:"Roboto Condensed",Arial,sans-serif;color:var(--navy);line-height:1}
  .section-title strong{display:block;font-size:42px;font-weight:700;letter-spacing:1px}
  .section-title span{display:block;font-size:22px;letter-spacing:1px;margin-top:2px}
  .service{position:absolute;background:var(--panel);border:1px solid var(--panel-line);color:var(--white);padding:14px 18px}
  .service h3{font-family:"Roboto Condensed",Arial,sans-serif;font-size:13px;font-weight:700;letter-spacing:.5px;text-transform:uppercase;margin-bottom:10px;white-space:nowrap}
  .service ul{list-style:none;font-size:10px;line-height:1.6;width:62%}
  .service p{font-size:10px;line-height:1.5;width:62%;margin-bottom:6px}
  .service .icon{position:absolute;right:20px;top:50%;transform:translateY(-50%);width:84px;height:84px;border-radius:8px;background:rgba(255,255,255,.08)}
  .svc-telecom{left:188px;top:175px;width:387px;height:162px}
  .svc-acesso{left:188px;top:350px;width:387px;height:150px}
  .svc-cftv{left:188px;top:512px;width:387px;height:150px}
  .svc-incendio{left:585px;top:8px;width:350px;height:150px}
  .svc-vagas{left:585px;top:172px;width:350px;height:200px}
  .svc-contrato{left:585px;top:386px;width:350px;height:162px}
  .tagline-band{position:absolute;left:0;top:675px;width:575px;height:130px;background:var(--blue);color:var(--white);padding:30px 30px 0 150px;font-family:"Roboto Condensed",Arial,sans-serif;font-size:27px;font-weight:700;line-height:1.05}
  .cover-title{position:absolute;left:950px;top:70px;width:190px;text-align:right;font-family:"Roboto Condensed",Arial,sans-serif;font-weight:700;color:var(--white);line-height:1}
  .cover-title span{display:block;font-size:34px;letter-spacing:.5px}
  .cover-title span:last-child{font-size:25px;margin-top:4px}
  .contact{position:absolute;left:835px;top:622px;width:305px;text-align:center;color:var(--ink)}
  .contact p{font-size:17px;font-weight:500;line-height:1.05}
  .contact .phone{font-size:30px;font-weight:500;margin-top:6px;letter-spacing:.5px}
</style>
</head>
<body>
<main class="brochure">
  <svg class="brochure__bg" width="1160" height="805" viewBox="0 0 1160 805" aria-hidden="true">
    <defs>
      <linearGradient id="coverBlue" x1="0" y1="0" x2="1" y2="1">
        <stop offset="0" stop-color="#0f5fc0"/><stop offset="1" stop-color="#1a8fe3"/>
      </linearGradient>
    </defs>
    <rect width="1160" height="805" fill="#eef5fc"/>
    <polygon points="0,640 575,640 575,805 0,805" fill="#dbe9f7"/>
    <polygon points="575,0 1160,0 1160,330 1000,560 575,560" fill="url(#coverBlue)"/>
    <polygon points="960,420 1160,280 1160,560 1000,560" fill="#4aa8ee" opacity=".6"/>
    <polygon points="130,575 185,575 140,635 85,635" fill="#ffffff"/>
    <polygon points="65,575 120,575 75,635 20,635" fill="#ffffff" opacity=".8"/>
    <polygon points="995,180 1040,180 990,260 945,260" fill="#ffffff"/>
    <polygon points="1055,180 1100,180 1050,260 1005,260" fill="#ffffff"/>
    <polygon points="1115,180 1160,180 1110,260 1065,260" fill="#ffffff"/>
    <polygon points="330,0 575,0 575,30 420,30" fill="#ffffff" opacity=".6"/>
  </svg>

  <div class="placeholder network-art" role="img" aria-label="Ilustração de rede com ícones de segurança conectados"></div>
  <div class="placeholder network-art--corner" role="img" aria-label="Ilustração decorativa de rede com ícones de tecnologia"></div>

  <h2 class="section-title"><strong>NOSSAS</strong><span>ESPECIALIDADES</span></h2>

  <section class="service svc-telecom">
    <h3>Engenharia de Telecom</h3>
    <ul><li>Cabeamento estruturado</li><li>Fibra óptica</li><li>PABX IP e digital</li><li>Redes sem fio</li><li>Instalação de racks</li><li>Manutenção preventiva</li><li>Projeto e consultoria</li></ul>
    <div class="icon" role="img" aria-label="Ícone de servidor de telecomunicações"></div>
  </section>

  <section class="service svc-acesso">
    <h3>Controle de Acesso</h3>
    <ul><li>Catracas e torniquetes</li><li>Leitores biométricos</li><li>Controle de portões</li><li>Cancelas automáticas</li><li>Software de gestão</li></ul>
    <div class="icon" role="img" aria-label="Ícone de catraca de controle de acesso"></div>
  </section>

  <section class="service svc-cftv">
    <h3>CFTV IP</h3>
    <ul><li>Câmeras IP de alta definição</li><li>Gravação em nuvem</li><li>Monitoramento remoto</li><li>Análise de vídeo</li><li>Projeto sob medida</li></ul>
    <div class="icon" role="img" aria-label="Ícone de câmera de vigilância"></div>
  </section>

  <section class="service svc-incendio">
    <h3>Detecção &amp; Combate a Incêndio</h3>
    <ul><li>Manutenção corretiva e preventiva</li><li>Detectores de fumaça</li><li>Alarmes e sirenes</li><li>Projeto e consultoria</li></ul>
    <div class="icon" role="img" aria-label="Ícone de detector de fumaça"></div>
  </section>

  <section class="service svc-vagas">
    <h3>Gerenciamento de Vagas Estacionamento</h3>
    <ul><li>Sensores de vaga</li><li>Painéis indicadores</li><li>Contagem de veículos</li><li>Sinalização por cores</li><li>Relatórios de ocupação</li><li>Integração com cancelas</li><li>Instalação rápida</li></ul>
    <div class="icon" role="img" aria-label="Ícone de placa de estacionamento"></div>
  </section>

  <section class="service svc-contrato">
    <h3>Contrato de Manutenção</h3>
    <p>Contratos sob medida para manter seus sistemas sempre ativos.</p>
    <ul><li>Atendimento 24 horas</li><li>Equipe técnica residente</li><li>Peças de reposição</li><li>Relatórios mensais</li></ul>
    <div class="icon" role="img" aria-label="Ícone de celular com engrenagens"></div>
  </section>

  <p class="tagline-band">Fornecemos mão de obra técnica especializada de manutenção</p>

  <h1 class="cover-title"><span>SISTEMAS</span><span>ESPECIAIS</span><span>INTEGRADOS</span></h1>

  <div class="placeholder portrait" role="img" aria-label="Foto de consultor de terno com braços cruzados"></div>

  <div class="contact">
    <p>Ligue e fale com um<br>de nossos consultores<br>e peça seu orçamento</p>
    <p class="phone">(21) 3555-0192</p>
  </div>
</main>
</body>
</html>
```